Book Cover - For Best Selling Diet

Hi
Book cover required for a diet book being marketed to become a best seller
For best quality, image will be 2820 pixels on the shortest side and 4500 pixels on the longest side .
The book name : Bright Morning Plan
By Corinna Plett
( will add in the extra text once we see design - top and bottom subtitle )
I do not want a photo of a person on the book.
PLEASE SEE " THE 9 STEP FRAME" by Ned Galbury as an example of solid style and I also love Quiet Ledger for the font.
Branding Colours:
#F26432
#A4195C
#A7D8CC
Font that runs through our brand is : helvetica neue
This is for a book that will be marketed for #1 bestseller - So please only quality
designs that are designed in a unique style.
Thanks
Target Market(s)
Busy Working Mums, Affluent, 30+ .
Look and feel

```html
<!DOCTYPE html>
<html lang="en">
<head>
<meta charset="utf-8">
<title>Bright Morning Plan — Corinna Plett</title>
<link rel="stylesheet" href="https://fonts.googleapis.com/css2?family=Inter:wght@100;200&display=swap">
<style>
  :root {
    --coral: #e35c46;
    --crimson: #cc2f50;
    --magenta: #a4195c;
    --mauve: #a25a82;
    --dusk: #a88a9a;
    --mist: #a9bcbc;
    --ink-light: #ffffff;
    --font-main: "Inter", "Helvetica Neue", Helvetica, Arial, sans-serif;
  }
  html, body {
    margin: 0;
    padding: 0;
    width: 930px;
    height: 1200px;
    overflow: hidden;
  }
  .book-cover {
    position: relative;
    width: 930px;
    height: 1200px;
    background: linear-gradient(
      to bottom,
      var(--coral) 0%,
      var(--crimson) 22%,
      var(--magenta) 48%,
      var(--mauve) 66%,
      var(--dusk) 82%,
      var(--mist) 100%
    );
    color: var(--ink-light);
    font-family: var(--font-main);
    text-align: center;
  }
  .title-kicker {
    position: absolute;
    top: 352px;
    left: 0;
    right: 0;
    margin: 0;
    font-weight: 200;
    font-size: 66px;
    letter-spacing: 2px;
    line-height: 1;
  }
  .title-main {
    position: absolute;
    top: 430px;
    left: 0;
    right: 0;
    margin: 0;
    font-weight: 100;
    font-size: 262px;
    letter-spacing: -4px;
    line-height: 1;
  }
  .byline {
    position: absolute;
    top: 748px;
    left: 0;
    right: 0;
    margin: 0;
    font-weight: 200;
    font-size: 60px;
    line-height: 1;
  }
  .author {
    position: absolute;
    top: 842px;
    left: 0;
    right: 0;
    margin: 0;
    font-weight: 200;
    font-size: 74px;
    letter-spacing: 1px;
    line-height: 1;
  }
</style>
</head>
<body>
  <main class="book-cover">
    <h1>
      <span class="title-kicker">BRIGHT MORNING</span>
      <span class="title-main">Plan</span>
    </h1>
    <p class="byline">BY</p>
    <p class="author">Corinna Plett</p>
  </main>
</body>
</html>
```